Business Card Design

We develop / design / build affordable housing throughout the state of Illinois.

Target Market(s)

non profit organizations and other developers / professionals in my industry

Industry/Entity Type

Business

Contact Information for Business Card

Birchstone Construction, LLC
General Contracting
Marisol K Thornbury, CEO
418 North Harlan W Ostrow Avenue, Suite 305
Harrowgate, IL 60499
555-555-0147
mkt@buildbirchstone.com

```html
<!DOCTYPE html>
<html lang="en">
<head>
<meta charset="utf-8">
<title>Birchstone Construction, LLC — Business Card</title>
<link href="https://fonts.googleapis.com/css2?family=Open+Sans:wght@400;600&display=swap" rel="stylesheet">
<style>
  :root {
    --canvas: #d9d9d9;
    --card-light: #f4f4f4;
    --card-light-edge: #e2e2e2;
    --card-dark: #2a2a2a;
    --ink: #2b2b2b;
    --ink-soft: #555555;
    --silver: #e6e6e6;
    --silver-soft: #bdbdbd;
  }
  html, body {
    margin: 0;
    padding: 0;
    width: 1200px;
    height: 900px;
    overflow: hidden;
    background: var(--canvas);
    font-family: "Open Sans", Arial, sans-serif;
  }
  .canvas {
    width: 1200px;
    height: 900px;
    display: flex;
    flex-direction: column;
    align-items: center;
    justify-content: center;
    gap: 40px;
  }
  .card {
    width: 700px;
    height: 400px;
    position: relative;
    box-sizing: border-box;
    overflow: hidden;
    box-shadow: 0 6px 18px rgba(0,0,0,0.18);
  }
  .skyline-art {
    position: absolute;
    border-radius: 4px;
  }

  /* Front: contact side */
  .card--front {
    background: linear-gradient(135deg, var(--card-light), var(--card-light-edge));
    color: var(--ink);
  }
  .card--front .skyline-art {
    left: 40px;
    top: 90px;
    width: 310px;
    height: 220px;
    background: linear-gradient(180deg, rgba(0,0,0,0.02), rgba(0,0,0,0.07));
  }
  .front-brand {
    position: absolute;
    left: 60px;
    top: 150px;
    width: 270px;
  }
  .front-brand .brand-name {
    font-size: 28px;
    font-weight: 600;
    line-height: 1.15;
    color: var(--ink);
    margin: 0;
  }
  .front-brand .brand-tagline {
    margin: 8px 0 0;
    font-size: 15px;
    color: var(--ink-soft);
  }
  .contact {
    position: absolute;
    left: 380px;
    top: 110px;
    width: 290px;
    font-size: 14px;
    line-height: 1.55;
  }
  .contact .person {
    font-size: 17px;
    font-weight: 600;
    font-variant: small-caps;
    letter-spacing: 0.5px;
    margin: 0;
  }
  .contact .role {
    font-size: 12px;
    margin: 0 0 18px;
    color: var(--ink-soft);
  }
  .contact-line {
    display: flex;
    align-items: center;
    gap: 8px;
    margin: 0;
  }
  .contact-line svg { flex: none; }
  .address { margin: 16px 0 0; }

  /* Back: brand side */
  .card--back {
    background: radial-gradient(ellipse at 40% 40%, #363636, var(--card-dark));
    color: var(--silver);
    display: flex;
    flex-direction: column;
    align-items: center;
    justify-content: center;
    text-align: center;
  }
  .card--back .skyline-art {
    left: 150px;
    top: 60px;
    width: 400px;
    height: 150px;
    background: linear-gradient(180deg, rgba(255,255,255,0.02), rgba(255,255,255,0.08));
  }
  .card--back .brand-name {
    position: relative;
    font-size: 40px;
    font-weight: 600;
    color: var(--silver);
    margin: 90px 0 0;
  }
  .card--back .brand-tagline {
    position: relative;
    margin: 8px 0 0;
    font-size: 20px;
    color: var(--silver-soft);
  }
</style>
</head>
<body>
<main class="canvas">
  <section class="card card--front" aria-label="Business card, contact side">
    <div class="skyline-art" role="img" aria-label="Faint city skyline line illustration"></div>
    <div class="front-brand">
      <p class="brand-name">Birchstone Construction, LLC</p>
      <p class="brand-tagline">General Contracting</p>
    </div>
    <div class="contact">
      <p class="person">Marisol K Thornbury</p>
      <p class="role">CEO</p>
      <p class="contact-line">
        <svg width="14" height="14" viewBox="0 0 14 14" aria-hidden="true">
          <rect width="14" height="14" rx="2" fill="#2b2b2b"/>
          <path d="M4 3.2c.5-.3 1-.2 1.3.3l.7 1.2c.2.4.1.8-.2 1.1l-.5.4c.4.9 1.1 1.6 2 2l.4-.5c.3-.3.7-.4 1.1-.2l1.2.7c.5.3.6.8.3 1.3l-.4.6c-.4.5-1 .7-1.6.5C6 10 4 8 3.4 5.7c-.2-.6 0-1.2.6-1.6z" fill="#f4f4f4"/>
        </svg>
        555-555-0147
      </p>
      <p class="contact-line">
        <svg width="14" height="14" viewBox="0 0 14 14" aria-hidden="true">
          <rect width="14" height="14" rx="2" fill="#2b2b2b"/>
          <rect x="2.5" y="4" width="9" height="6" fill="none" stroke="#f4f4f4" stroke-width="1"/>
          <path d="M2.5 4l4.5 3.5L11.5 4" fill="none" stroke="#f4f4f4" stroke-width="1"/>
        </svg>
        mkt@buildbirchstone.com
      </p>
      <p class="address">418 North Harlan W Ostrow Avenue,<br>Suite 305, Harrowgate, IL 60499</p>
    </div>
  </section>

  <section class="card card--back" aria-label="Business card, brand side">
    <div class="skyline-art" role="img" aria-label="Silver city skyline line illustration"></div>
    <p class="brand-name">Birchstone Construction, LLC</p>
    <p class="brand-tagline">General Contracting</p>
  </section>
</main>
</body>
</html>
```